Business Card Design

Quiet Meadows - edgy, unique, ontrend clothing for girls 0-12.
I would like simple styling with white background and natural beige/brown font, similar to attached font.

Industry/Entity Type

Clothing

Contact Information for Business Card

Hi, I would like a very simple business card, white background with natural, beige, brown font, Quiet Meadows. I design and sell clothes for girls 0-12 with a touch of bohemian styling. I would like "Quiet Meadows" on front and on back -
www.quietmeadows-example.com.au
Delia Hartwell,
0481552937,
deliahartwell@brightnest-mail.com.au

```html
<!DOCTYPE html>
<html lang="en">
<head>
<meta charset="utf-8">
<title>Quiet Meadows – Business Card</title>
<link rel="stylesheet" href="https://fonts.googleapis.com/css2?family=Indie+Flower&display=swap">
<style>
  :root {
    --stage-top: #e4e4e4;
    --stage-bottom: #c9c9c9;
    --card-cream: #efe8dc;
    --card-sand: #e6dccb;
    --card-lavender: #d8d0dc;
    --ink-brown: #9e916f;
    --ink-soft: #b0a283;
    --card-shadow: rgba(60, 55, 50, 0.22);
  }
  * { box-sizing: border-box; margin: 0; padding: 0; }
  html, body {
    width: 1200px;
    height: 960px;
    overflow: hidden;
  }
  body {
    background: linear-gradient(180deg, var(--stage-top), var(--stage-bottom));
    font-family: "Indie Flower", cursive;
    position: relative;
  }
  .business-card {
    position: absolute;
    left: 180px;
    top: 240px;
    width: 840px;
    height: 480px;
    border-radius: 4px;
    overflow: hidden;
    box-shadow: 0 14px 34px var(--card-shadow);
  }
  .card-pattern {
    position: absolute;
    inset: 0;
    background:
      radial-gradient(ellipse at 85% 20%, var(--card-lavender) 0%, transparent 55%),
      radial-gradient(ellipse at 10% 95%, var(--card-lavender) 0%, transparent 50%),
      linear-gradient(160deg, var(--card-cream) 0%, var(--card-sand) 60%, var(--card-lavender) 100%);
  }
  .card-content {
    position: relative;
    height: 100%;
    color: var(--ink-brown);
  }
  .brand-name {
    position: absolute;
    left: 40px;
    top: 18px;
    font-size: 76px;
    font-weight: 400;
    letter-spacing: 2px;
  }
  .owner-name {
    position: absolute;
    left: 290px;
    top: 150px;
    font-size: 56px;
    font-weight: 400;
    letter-spacing: 3px;
    color: var(--ink-soft);
  }
  .contact-list {
    position: absolute;
    right: 36px;
    top: 258px;
    list-style: none;
    text-align: right;
    font-size: 24px;
    letter-spacing: 1px;
    line-height: 1;
  }
  .contact-list li { margin-bottom: 28px; }
</style>
</head>
<body>
  <section class="business-card">
    <div class="card-pattern" role="img" aria-label="Soft cream and lavender background with a faint bohemian floral and paisley pattern"></div>
    <div class="card-content">
      <h1 class="brand-name">Quiet Meadows</h1>
      <p class="owner-name">Delia Hartwell</p>
      <ul class="contact-list">
        <li class="contact-web">www.quietmeadows-example.com.au</li>
        <li class="contact-phone">0481552937</li>
        <li class="contact-email">deliahartwell@brightnest-mail.com.au</li>
      </ul>
    </div>
  </section>
</body>
</html>
```